Oak Bend Diesel & Trailer Repair needs a logo and business cards*

We need a logo design and cards for a new business in camilla, ga called Oak Bend Diesel & Trailer Repair. I would like a design with a Hallorway or Drummoke Semi on it and a gray background card with maybe red and white writing. Address is 517 Marsh Hollow Road Redmarsh, Ox 31884 phone is 229-555-0147 Wesley Hardcastle 229-555-0182, Danny Whitlow 229-555-0163 email address oakbenddieselandtrailer@mailexample.net offic enumber is 229-555-0147

Target Market(s)

people needing truck repairs

Logo Text

Oak Bnd Diesel & Trailer Repair

Logo styles of interest
Wordmark Logo
Font styles to use
Serif
Sans Serif

Colors

Designer to choose colors to be used in the design.

Requirements
Must have
• names, address, phone number, email address and a picture of a Hallorway or Drummoke Semi
• i attached a picture of a card that I would like a card similar to
Nice to have
• i would like it it double sided- on the back i want
• We specialize in DOT inspections, Preventative maintenance, Brake repair, Clutch repair, tire repair, on and off site diagnostics, service calls
• Trailer repair

```html
<!DOCTYPE html>
<html lang="en">
<head>
<meta charset="utf-8">
<title>Oak Bend Diesel &amp; Trailer Repair – Business Card</title>
<link rel="stylesheet" href="https://fonts.googleapis.com/css2?family=Lato:wght@400;700&display=swap">
<style>
  :root {
    --backdrop: #d1d2d4;
    --card: #3b3b3d;
    --card-weave: #434345;
    --ink-light: #ffffff;
    --brand-red: #a3232b;
    --truck-red: #b3212a;
    --truck-silver: #c9cbce;
  }
  html, body {
    margin: 0;
    width: 1200px;
    height: 960px;
    overflow: hidden;
    background: var(--backdrop);
    font-family: "Lato", sans-serif;
  }
  .business-card {
    position: absolute;
    left: 50px;
    top: 165px;
    width: 1100px;
    height: 629px;
    background-color: var(--card);
    background-image:
      repeating-linear-gradient(0deg, var(--card-weave) 0 1px, transparent 1px 4px),
      repeating-linear-gradient(90deg, var(--card-weave) 0 1px, transparent 1px 4px);
    color: var(--ink-light);
  }
  .holder-name {
    position: absolute;
    left: 64px;
    top: 96px;
    margin: 0;
    font-size: 48px;
    font-weight: 700;
    line-height: 1;
    letter-spacing: 0.5px;
  }
  .holder-title {
    position: absolute;
    left: 64px;
    top: 152px;
    margin: 0;
    font-size: 29px;
    font-weight: 400;
  }
  .phone-list {
    position: absolute;
    left: 64px;
    top: 242px;
    margin: 0;
    font-size: 26px;
    line-height: 31px;
  }
  .wordmark {
    position: absolute;
    left: 530px;
    top: 82px;
    color: var(--brand-red);
    font-weight: 700;
  }
  .wordmark-name {
    display: block;
    font-size: 88px;
    line-height: 0.95;
  }
  .wordmark-tag {
    display: block;
    font-size: 32px;
    letter-spacing: 1px;
    text-transform: uppercase;
    margin-top: 8px;
  }
  .address {
    position: absolute;
    left: 566px;
    top: 322px;
    margin: 0;
    font-style: normal;
    font-size: 26px;
    line-height: 31px;
  }
  .contact {
    position: absolute;
    left: 569px;
    top: 428px;
    margin: 0;
    font-size: 26px;
    line-height: 34px;
  }
  .truck-photo {
    position: absolute;
    left: 57px;
    top: 436px;
    width: 290px;
    height: 184px;
    border-radius: 10px 40px 4px 4px;
    background: linear-gradient(90deg, var(--truck-red) 0%, var(--truck-red) 52%, var(--truck-silver) 60%, var(--truck-silver) 100%);
  }
</style>
</head>
<body>
  <section class="business-card">
    <h1 class="holder-name">YOUR NAME</h1>
    <p class="holder-title">Title</p>
    <p class="phone-list">
      229-555-0147<br>
      Wesley Hardcastle 229-555-0182,<br>
      Danny Whitlow 229-555-0163
    </p>

    <div class="wordmark">
      <span class="wordmark-name">Oak Bnd</span>
      <span class="wordmark-tag">Diesel &amp; Trailer Repair</span>
    </div>

    <address class="address">
      517 Marsh Hollow Road Redmarsh,<br>
      Ox 31884
    </address>

    <p class="contact">
      oakbenddieselandtrailer@mailexample.net<br>
      offic enumber is 229-555-0147
    </p>

    <div class="truck-photo" role="img" aria-label="Photo of a red semi truck with a silver trailer"></div>
  </section>
</body>
</html>
```